Construction business card

We are a family run and family oriented business in Philadelphia and we are starting new. We proudly serve the public by giving our customers great work at affordable prices. We can do all aspects of construction from the roof to the basement. We would like our business card to incorporate tools and family.
Updates

Can y'all please incorporate a bulldog

Industry/Entity Type

Construction

Contact Information for Business Card

Harbor Builders LLC, Dennis Whitcomb, 1187 W 9th st Philadelphia Pa 19140, CEO Main phone (215) 555-0143 cellphone 215-555-0187 Dennis whitcomb Jr cellphone 267-555-0129 email harborbuildersllc@quillpost.example

Colors
f78f20
ffffff
1b1b1b

```html
<!DOCTYPE html>
<html lang="en">
<head>
<meta charset="utf-8">
<title>Harbor Builders LLC – Business Card</title>
<link href="https://fonts.googleapis.com/css2?family=Open+Sans:ital,wght@0,400;0,600;0,700;1,400&display=swap" rel="stylesheet">
<style>
  :root {
    --orange: #f78f20;
    --orange-light: #fbad3c;
    --white: #ffffff;
    --ink: #1b1b1b;
    --grey-text: #6a6a6a;
    --stage: #ececec;
    --dog-light: #e2e2e2;
    --dog-dark: #9a9a9a;
  }
  * { box-sizing: border-box; margin: 0; padding: 0; }
  html, body {
    width: 1200px; height: 576px; overflow: hidden;
    background: var(--stage);
    font-family: "Open Sans", Arial, sans-serif;
    color: var(--ink);
  }
  .stage {
    width: 1200px; height: 576px;
    display: flex; align-items: center; justify-content: center; gap: 40px;
  }
  .card {
    position: relative;
    width: 540px; height: 310px;
    background: var(--white);
    overflow: hidden;
    box-shadow: 0 6px 18px rgba(0,0,0,.18);
  }
  .card-band { position: absolute; inset: 0; }

  /* back side */
  .contact {
    position: absolute; top: 24px; right: 36px;
    text-align: right; font-size: 15px; line-height: 1.5;
  }
  .contact .person {
    font-weight: 700; color: var(--grey-text); font-size: 18px;
  }
  .contact .person + .row { margin-top: 2px; }
  .contact .label { font-style: italic; color: var(--orange); }
  .contact .value { color: var(--ink); }
  .contact .second { margin-top: 12px; }
  .band-name {
    position: absolute; left: 36px; bottom: 28px;
    font-size: 32px; font-weight: 700; color: var(--ink);
  }

  /* front side */
  .brand-name {
    position: absolute; top: 40px; left: 0; right: 0;
    text-align: center;
    font-size: 40px; font-weight: 700; color: var(--ink);
    letter-spacing: .5px;
  }
  .mascot {
    position: absolute; left: 255px; top: 110px;
    width: 120px; height: 108px; border-radius: 46%;
    background: radial-gradient(circle at 50% 40%, var(--dog-light), var(--dog-dark));
  }
  .address {
    position: absolute; left: 34px; bottom: 44px;
    display: flex; align-items: center; gap: 12px;
    font-size: 24px; color: var(--ink);
  }
  .address svg { flex: none; }
</style>
</head>
<body>
<main class="stage">

  <section class="card card-back" aria-label="Card back">
    <svg class="card-band" viewBox="0 0 540 310" aria-hidden="true">
      <path d="M0 175 H290 V206 Q290 226 310 226 H516 Q536 226 536 206 V175 H540 V310 H0 Z" fill="var(--orange)"/>
    </svg>
    <div class="contact">
      <p class="person">Dennis Whitcomb, CEO</p>
      <p class="row"><span class="label">CEO main phone</span> <span class="value">(215) 555-0143</span></p>
      <p class="row"><span class="label">cellphone</span> <span class="value">215-555-0187</span></p>
      <p class="row"><span class="label">email</span> <span class="value">harborbuildersllc@quillpost.example</span></p>
      <p class="person second">Dennis whitcomb Jr</p>
      <p class="row"><span class="label">cellphone</span> <span class="value">267-555-0129</span></p>
    </div>
    <p class="band-name">Harbor Builders LLC</p>
  </section>

  <section class="card card-front" aria-label="Card front">
    <svg class="card-band" viewBox="0 0 540 310" aria-hidden="true">
      <defs>
        <linearGradient id="bandGlow" x1="0" y1="0" x2="1" y2="0">
          <stop offset="0" stop-color="var(--orange-light)"/>
          <stop offset="1" stop-color="var(--orange)"/>
        </linearGradient>
      </defs>
      <path d="M0 175 H200 V200 Q200 222 222 222 H408 Q430 222 430 200 V175 H540 V310 H0 Z" fill="url(#bandGlow)"/>
    </svg>
    <p class="brand-name">Harbor Builders LLC</p>
    <div class="mascot" role="img" aria-label="Bulldog mascot illustration with crossed arms"></div>
    <p class="address">
      <svg width="24" height="22" viewBox="0 0 24 22" aria-hidden="true">
        <path d="M12 1 L23 11 H19.5 V21 H14.5 V14 H9.5 V21 H4.5 V11 H1 Z" fill="var(--white)"/>
      </svg>
      1187 W 9th st Philadelphia Pa 19140
    </p>
  </section>

</main>
</body>
</html>
```